Business Card Design Project

We need a business card design for a new company based in Singapore called 'Bright Harbor Pte Ltd'. We provide personal development training and emotional intelligence workshops. Our slogan is "Actualize your potentials". We will not have a company address on the business card. Only phone number, email address and website address.

Target Market(s)

Adults age 25 to 45 years old.
Mostly working in a job.

Industry/Entity Type

Training

Colors
0255a2
f37123

```html
<!DOCTYPE html>
<html lang="en">
<head>
<meta charset="utf-8">
<title>Bright Harbor Pte Ltd – Business Card</title>
<link rel="stylesheet" href="https://fonts.googleapis.com/css2?family=Roboto:wght@300;400;700&display=swap">
<style>
  :root {
    --stage: #000000;
    --paper: #ffffff;
    --navy: #0b1c6b;
    --orange: #ff4000;
    --slogan-soft: #7d8cc8;
  }
  * { margin: 0; padding: 0; box-sizing: border-box; }
  html, body {
    width: 1200px;
    height: 447px;
    overflow: hidden;
    background: var(--stage);
    font-family: "Roboto", Arial, sans-serif;
  }
  .stage { position: relative; width: 1200px; height: 447px; }
  .card {
    position: absolute;
    top: 67px;
    width: 530px;
    height: 312px;
    overflow: hidden;
  }
  .card svg { position: absolute; inset: 0; }
  .card--front { left: 70px; background: var(--paper); }
  .card--back { left: 600px; background: var(--navy); }

  .brand {
    position: absolute;
    left: 168px;
    top: 36px;
    display: flex;
    align-items: center;
    gap: 10px;
    color: var(--navy);
    font-weight: 700;
  }
  .brand__dot {
    width: 34px; height: 34px;
    border-radius: 50%;
    border: 3px solid var(--navy);
  }
  .brand__name { font-size: 22px; line-height: 1; letter-spacing: -0.3px; }
  .brand__suffix {
    display: block;
    font-size: 11px;
    letter-spacing: 1px;
    text-align: right;
    margin-top: 4px;
  }

  .slogan {
    position: absolute;
    left: 0; right: 0;
    text-align: center;
    font-weight: 300;
    font-size: 26px;
    letter-spacing: -0.2px;
  }
  .card--front .slogan { top: 190px; color: var(--slogan-soft); }
  .card--back .slogan { top: 70px; color: var(--paper); }

  .contact {
    position: absolute;
    left: 145px;
    width: 242px;
    top: 214px;
    text-align: center;
    color: var(--navy);
    font-size: 14px;
    line-height: 22px;
    list-style: none;
  }
  .contact strong { font-weight: 700; }
</style>
</head>
<body>
<main class="stage">
  <section class="card card--front">
    <svg width="530" height="312" viewBox="0 0 530 312" aria-hidden="true">
      <circle cx="253" cy="12" r="143" fill="var(--navy)"/>
      <circle cx="264" cy="11" r="132" fill="var(--paper)"/>
    </svg>
    <div class="brand">
      <span class="brand__dot"></span>
      <div>
        <span class="brand__name">Bright Harbor</span>
        <span class="brand__suffix">PTE LTD</span>
      </div>
    </div>
    <p class="slogan">Actualize Your Potentials</p>
  </section>

  <section class="card card--back">
    <svg width="530" height="312" viewBox="0 0 530 312" aria-hidden="true">
      <circle cx="278" cy="298" r="143" fill="var(--orange)"/>
      <circle cx="268" cy="300" r="132" fill="var(--paper)"/>
    </svg>
    <p class="slogan">Actualize Your Potentials</p>
    <ul class="contact">
      <li>Ph. 010 220 004 300</li>
      <li>e-mail : info@brightharbor.com</li>
      <li>web : www.<strong>brightharbor</strong>.com</li>
    </ul>
  </section>
</main>
</body>
</html>
```